Renamed Motel Needs Appealing Flyer

We need a flyer design for a motel that has been closed for 3 years and has just reopened under new management. It has been renamed 'Torvanne Motel' and is located in the Grampians in Vic. We would like our design to showcase the beauty and magnificence of the Grampians National Park (Gariwerd being the Aboriginal name for the Park). The motel is an older style building, so we don't want photos of the building to be the focus of the flyer until we have had time to renovate etc.
http://www.filedrift.com/file/8kq2pz
I will add a high res image of the motel name/logo on Monday
http://www.filedrift.com/file/8kq2pz to see an additional photo. I will add a high res image of motel name/logo on Monday
Target Market(s)
all ages, backpackers, budget consious travellers, seniors, groups
Industry/Entity Type
Building
Requirements
Must have
- Flyer must be DL size (front and back only) with logo at the top so that it is visible when displayed in a tiered display rack. I am not sure if the logo I have provided is adequate resolution wise. Can you let me know if it is not? The 'points' under the name are not part of the logo and should be removed.
Suggested wording for front of flyer - Surrounded by rugged mountain ranges and native plants and animals, Torvanne Motel is the perfect base to explore the natural beauty of the Grampians.
Back of flyer - features: affordable accommodation, 25 spacious ground floor rooms,
single/twin/triple/quadruple rooms; queen beds; ensuite bathrooms/some rooms with baths; toaster/ tea and coffee making facilities; iron/ironing board in rooms; digital TV; free WiFi; microwaves for guest use; free BBQ facilities; breakfast available; conference facility for up to 25 persons
Address - 14 Wattlebark Rd, Fernvale Flat 3392
Phone: (03) 5412 7780
Email: torvannemotel@quillnet.com
www.torvannemotel.com.au
Updated after first set of submissions/comments - 10.55 PM AEST.
The following text only should be for the front of the brochure - Surrounded by rugged mountain ranges and native plants and animals, Torvanne Motel is the perfect base to explore the natural beauty of the Grampians.
Logically then, listings from the original brief such as 'Surrounded by mountains' would not be relevant for the back.
The dot points listed above in the first brief, should then be the focus for the information and detail on the back of the brochure.
Another update is;
- correct display is T/Rail
Nice to have
- I would like the flyer to have a flowing feel, print over top of scenery images, different fonts. Perhaps back of flyer could be printed over a washed image of Grampians

```html
<!DOCTYPE html>
<html lang="en">
<head>
<meta charset="utf-8">
<title>Torvanne Motel – DL Flyer</title>
<link rel="stylesheet" href="https://fonts.googleapis.com/css2?family=Roboto+Condensed:wght@700&family=Source+Sans+3:wght@600;700&display=swap">
<style>
  :root{
    --backdrop:#ece7df;
    --forest:#1f5a24;
    --forest-deep:#17481b;
    --leaf:#6cbf3a;
    --lime:#9bd04a;
    --gold:#e5c12b;
    --heading-gold:#e3c12c;
    --cream:#f3efcf;
    --ink:#1d1d1b;
    --white:#ffffff;
  }
  *{box-sizing:border-box;margin:0;padding:0}
  html,body{width:1200px;height:1178px;overflow:hidden}
  body{background:var(--backdrop);font-family:"Source Sans 3",sans-serif;position:relative}

  .flyer{position:absolute;top:72px;width:486px;height:1030px;overflow:hidden;box-shadow:0 4px 14px rgba(0,0,0,.35)}
  .flyer--front{left:105px}
  .flyer--back{left:628px}
  .flyer__art{position:absolute;inset:0;width:100%;height:100%}

  /* front */
  .brand-name{position:absolute;left:0;right:0;top:470px;text-align:center;font-family:"Source Sans 3",sans-serif;font-weight:700;font-size:52px;color:var(--cream);letter-spacing:1px}
  .section-title{font-family:"Roboto Condensed",sans-serif;font-weight:700;color:var(--heading-gold);letter-spacing:.3px}
  .advantages{position:absolute;left:30px;top:608px;right:0}
  .advantages .section-title{font-size:30px}
  .advantages__list{list-style:none;margin-top:22px}
  .advantages__list li{position:relative;padding-left:28px;color:var(--white);font-weight:600;font-size:21.5px;line-height:29px;margin-bottom:11px;padding-right:40px}
  .advantages__list li::before{content:"";position:absolute;left:0;top:8px;width:15px;height:15px;border-radius:50%;background:radial-gradient(circle at 35% 35%,#f4f4f4,#a9a9a9)}
  .call{position:absolute;left:0;right:0;top:968px;text-align:center;color:var(--ink);font-family:"Roboto Condensed",sans-serif;font-weight:700}
  .call__label{font-size:20px;text-transform:uppercase}
  .call__number{font-size:38px;margin-left:4px}

  /* back */
  .facilities{position:absolute;left:38px;top:30px;right:20px}
  .facilities .section-title{font-size:32px}
  .facilities__list{list-style:none;margin-top:22px}
  .facilities__list li{position:relative;padding-left:38px;color:var(--white);font-weight:600;font-size:22.5px;line-height:29px;margin-bottom:11px}
  .facilities__list li::before{content:"";position:absolute;left:6px;top:6px;width:7px;height:13px;border:solid #e8e8e8;border-width:0 3px 3px 0;transform:rotate(40deg)}
  .map{position:absolute;left:210px;top:688px}
  .location-name{position:absolute;left:25px;top:740px;font-family:"Roboto Condensed",sans-serif;font-weight:700;font-size:26px;color:var(--lime)}
  .address{position:absolute;left:200px;width:290px;top:818px;text-align:center;font-family:"Roboto Condensed",sans-serif;font-weight:700;font-size:28px;line-height:37px;color:var(--white);text-shadow:0 1px 2px rgba(0,0,0,.45)}
  .contact{position:absolute;left:0;right:0;top:926px;text-align:center;color:var(--ink)}
  .contact__label{font-family:"Roboto Condensed",sans-serif;font-weight:700;font-size:17px}
  .contact__email{font-weight:600;font-size:26px;margin-top:2px}
  .contact__web{font-weight:600;font-size:16px;letter-spacing:3.4px;margin-top:4px}
</style>
</head>
<body>

<section class="flyer flyer--front">
  <svg class="flyer__art" viewBox="0 0 486 1030" preserveAspectRatio="none" aria-hidden="false">
    <defs>
      <linearGradient id="photoTone" x1="0" y1="0" x2="0" y2="1">
        <stop offset="0" stop-color="#5f8f3c"/>
        <stop offset=".6" stop-color="#7ea04c"/>
        <stop offset="1" stop-color="#9a9a88"/>
      </linearGradient>
    </defs>
    <rect width="486" height="1030" fill="var(--forest)"/>
    <path d="M0 960 Q260 900 486 835 V1030 H0Z" fill="#2e7a2b"/>
    <path role="img" aria-label="Photo of a family walking with a pram along a leafy path" d="M0 0 H486 V318 Q280 420 0 402Z" fill="url(#photoTone)"/>
    <path d="M0 402 Q280 420 486 318 V340 Q300 440 0 414Z" fill="var(--lime)"/>
    <path d="M0 414 Q300 440 486 340 V360 Q300 450 0 428Z" fill="var(--forest-deep)"/>
    <line x1="150" y1="637" x2="486" y2="637" stroke="#7fa77a" stroke-width="1"/>
    <path d="M0 935 Q270 915 486 860 V872 Q270 930 0 948Z" fill="var(--lime)"/>
    <path d="M0 948 Q270 930 486 872 V1030 H0Z" fill="var(--gold)"/>
  </svg>
  <div class="brand-name">Torvanne Motel</div>
  <div class="advantages">
    <h2 class="section-title">Advantages</h2>
    <ul class="advantages__list">
      <li>Surrounded by the mountains</li>
      <li>Motel is an easy 5 minute walk from the centre of Fernvale Flat</li>
      <li>100 metres from T-Rail Bus stop</li>
      <li>Affordable accommodation</li>
      <li>25 spacious ground floor rooms</li>
    </ul>
  </div>
  <div class="call"><span class="call__label">Call today:</span><span class="call__number">(03) 5412 7780</span></div>
</section>

<section class="flyer flyer--back">
  <svg class="flyer__art" viewBox="0 0 486 1030" preserveAspectRatio="none">
    <defs>
      <linearGradient id="backTone" x1="0" y1="0" x2="1" y2=".2">
        <stop offset="0" stop-color="#1d5f22"/>
        <stop offset=".55" stop-color="#2f8a2c"/>
        <stop offset="1" stop-color="#67b83a"/>
      </linearGradient>
    </defs>
    <rect width="486" height="1030" fill="url(#backTone)"/>
    <path d="M190 0 Q380 20 486 110 V0Z" fill="var(--lime)"/>
    <path d="M230 0 Q400 30 486 90 V0Z" fill="#5fb036"/>
    <path d="M0 790 Q160 860 486 872 V890 Q160 880 0 812Z" fill="var(--lime)"/>
    <path d="M0 812 Q160 880 486 890 V1030 H0Z" fill="#2e7a2b"/>
    <path d="M0 840 Q180 900 486 902 V1030 H0Z" fill="var(--gold)"/>
  </svg>
  <div class="facilities">
    <h2 class="section-title">Facilities</h2>
    <ul class="facilities__list">
      <li>Single / Twin / Triple /<br>Quadruple Rooms</li>
      <li>Queen beds</li>
      <li>Ensuite bathrooms /<br>some rooms with baths</li>
      <li>Toaster/ Tea &amp; coffee making<br>facilities</li>
      <li>Iron / Ironing board in rooms</li>
      <li>Digital TV</li>
      <li>Free WiFi</li>
      <li>Microwaves for guest use</li>
      <li>Free BBQ facilities</li>
      <li>Breakfast available</li>
      <li>Conference facility for up to<br>25 persons</li>
    </ul>
  </div>
  <svg class="map" width="256" height="132" viewBox="0 0 256 132">
    <ellipse role="img" aria-label="Street map showing the motel location" cx="128" cy="66" rx="126" ry="64" fill="#ecefe8" stroke="#ffffff" stroke-width="2"/>
  </svg>
  <div class="location-name">Torvanne Motel</div>
  <div class="address">14 Wattlebark Rd<br>Fernvale Flat 3392</div>
  <div class="contact">
    <div class="contact__label">Email:</div>
    <div class="contact__email">torvannemotel@quillnet.com</div>
    <div class="contact__web">www.torvannemotel.com.au</div>
  </div>
</section>

</body>
</html>
```